glow 742 is renewing its image

more dynamic website, make it look more attractive for the services we offer, at the same time more accurate on the services description. We want people to know we offer treatments that big corporations offer but not as expensive as they offer it. prices will be add by me once the website is approve
Updates

already have a website with wix.com www.glow742dermis.com

Target Market(s)

women between 21 to 75

Industry/Entity Type

beauty services, body contouring

Colors

Designer to choose colors to be used in the design.

Requirements
Must have
• pictures of treatments
Nice to have
• accurate information about treatmnets, treatments menu
Should not have
• no online shopping

```html
<!DOCTYPE html>
<html lang="en">
<head>
<meta charset="utf-8">
<title>Glow 742 Skin Lounge</title>
<link href="https://fonts.googleapis.com/css2?family=Playball&family=Roboto:wght@400;500;700&display=swap" rel="stylesheet">
<style>
:root{
  --brown:#7b4a1e;
  --brown-dark:#5e3512;
  --tan:#cd9f74;
  --cream:#fbf6f1;
  --ink:#231f20;
  --text:#6f6a66;
  --white:#ffffff;
}
*{box-sizing:border-box;margin:0;padding:0}
html,body{width:1200px;height:3684px;overflow:hidden}
body{position:relative;background:var(--cream);font-family:'Roboto',sans-serif;color:var(--text)}
.abs{position:absolute}
.script{font-family:'Playball',cursive;font-weight:400}
.btn{position:absolute;background:var(--brown);color:var(--white);border-radius:26px;font:700 15px 'Roboto',sans-serif;display:flex;align-items:center;justify-content:center;text-transform:uppercase;letter-spacing:.2px}
.fill{position:absolute}

/* header */
.site-header{position:absolute;left:0;top:0;width:1200px;height:97px;background:var(--cream);z-index:3}
.brand-tab{position:absolute;left:90px;top:0;width:220px;height:131px;background:var(--cream);clip-path:polygon(0 0,100% 0,100% 80%,90% 100%,10% 100%,0 80%);z-index:4;display:flex;align-items:center;justify-content:center;gap:10px}
.brand-tab .dot{width:14px;height:14px;border-radius:50%;background:var(--brown)}
.brand-tab .name{font:500 30px 'Roboto',sans-serif;color:var(--brown)}
.main-nav{position:absolute;left:376px;top:38px;display:flex;gap:23px;font:500 15px 'Roboto',sans-serif;color:#2a2420}
.phone-box{position:absolute;left:942px;top:0;width:258px;height:97px;background:var(--brown);color:var(--white);font:700 28px 'Roboto',sans-serif;display:flex;align-items:center;justify-content:center}

/* hero */
.hero-photo{left:0;top:97px;width:1200px;height:700px;background:linear-gradient(90deg,#efe2cf 0%,#f3dec4 35%,#e4e89a 65%,#a9cf3e 100%)}
.hero-wave{left:0;top:640px;width:1200px;height:160px}
.welcome-box{left:601px;top:276px;width:486px;height:203px;background:rgba(255,255,255,.82);text-align:center}
.welcome-box h1{font-size:31px;line-height:40px;color:var(--ink);margin-top:20px}

/* about */
.section-title{font-size:38px;color:var(--ink)}
.section-title span{color:var(--brown)}
.about-title{left:112px;top:865px}
.body-copy{font-size:14px;line-height:25px;text-align:justify}
.about-copy{left:112px;top:932px;width:416px}
.about-copy p+p{margin-top:12px}
.about-frame{left:626px;top:849px;width:462px;height:362px;border:6px solid var(--brown)}
.about-photo{left:611px;top:866px;width:460px;height:361px;background:var(--white);border-bottom-left-radius:60px;padding:6px}
.about-photo div{width:100%;height:100%;border-bottom-left-radius:56px;background:linear-gradient(135deg,#3a2a20 0%,#e8dcb8 35%,#e7dbbf 70%,#6a4a32 100%)}

/* treatments */
.treat-band{left:0;top:1323px;width:1200px;height:290px;background:linear-gradient(90deg,#2b2623,#3a332e 50%,#2b2623)}
.treat-title{left:0;top:1355px;width:1200px;text-align:center;color:var(--white);font-size:38px}
.round-arrow{position:absolute;width:34px;height:34px;border-radius:50%;background:var(--white);display:flex;align-items:center;justify-content:center}
.treat-card{position:absolute;top:1441px;width:313px;height:344px}
.treat-card .label{position:absolute;left:0;bottom:16px;width:100%;text-align:center;color:var(--white);font:500 17px/28px 'Roboto',sans-serif;text-transform:uppercase}
.treat-card.featured{background:#9a6535;color:var(--white);text-align:center;padding:0 32px}
.treat-card.featured h3{font:500 18px 'Roboto',sans-serif;margin-top:129px;text-transform:uppercase}
.treat-card.featured p{font-size:13px;line-height:25px;margin-top:18px}
.treat-card.featured a{display:inline-block;margin-top:20px;font:500 13px 'Roboto',sans-serif;text-decoration:underline;color:var(--white)}
.treat-icon{position:absolute;left:126px;top:38px}

/* post surgery */
.post-frame{left:112px;top:1897px;width:462px;height:360px;border:6px solid var(--brown)}
.post-photo{left:127px;top:1879px;width:462px;height:362px;background:var(--white);border-top-right-radius:60px;padding:6px}
.post-photo div{width:100%;height:100%;border-top-right-radius:56px;background:linear-gradient(90deg,#d9b89a 0%,#c08a5c 30%,#a46a3e 60%,#efe7df 85%,#fff 100%)}
.post-title{left:672px;top:1898px}
.post-copy{left:672px;top:1969px;width:416px}

/* before after */
.ba-band{left:0;top:2352px;width:1200px;height:514px;background:var(--tan)}
.ba-title{left:0;top:2393px;width:1200px;text-align:center;color:var(--white);font-size:38px}
.ba-card{position:absolute;top:2487px;width:428px;height:324px;background:var(--cream);padding:6px}
.ba-card .shot{height:259px;background:linear-gradient(180deg,#e9e9ec 0%,#dcd4c8 60%,#c9b9a5 100%)}
.ba-card .cap{text-align:center;font:500 20px 'Roboto',sans-serif;color:var(--brown);margin-top:16px}

/* newsletter */
.news-title{left:0;top:2940px;width:1200px;text-align:center;font-size:30px;color:var(--ink)}
.news-title span{color:var(--brown)}
.news-sub{left:0;top:2995px;width:1200px;text-align:center;font-size:20px;color:#3c3631}
.news-form{left:256px;top:3054px;width:686px;height:50px;border-radius:26px;background:var(--white);box-shadow:0 2px 6px rgba(0,0,0,.18);display:flex;overflow:hidden}
.news-form .field{flex:1;padding-left:25px;display:flex;align-items:center;font:500 15px 'Roboto',sans-serif;color:#4a4440}
.news-form .submit{width:138px;background:var(--brown);color:var(--white);font:700 15px 'Roboto',sans-serif;display:flex;align-items:center;justify-content:center;text-transform:uppercase}

/* footer */
.footer-wave{left:0;top:3170px;width:1200px;height:514px}
.footer-nav{left:0;top:3356px;width:1200px;display:flex;justify-content:center;gap:27px;color:var(--white);font:500 18px 'Roboto',sans-serif;text-transform:uppercase}
.footer-rule{position:absolute;height:1px;background:#55504c}
.footer-brand{left:500px;top:3425px;width:200px;display:flex;align-items:center;justify-content:center;gap:9px}
.footer-brand .dot{width:12px;height:12px;border-radius:50%;background:var(--white)}
.footer-brand .name{font:500 28px 'Roboto',sans-serif;color:var(--white)}
.footer-col{position:absolute;top:3510px;width:326px;text-align:center;color:var(--white);font:500 17px/26px 'Roboto',sans-serif}
.footer-col svg{display:block;margin:0 auto 14px}
.footer-divider{position:absolute;top:3439px;width:1px;height:189px;background:#55504c}
.copyright{left:112px;top:3647px;color:var(--white);font-size:12px}
.social{position:absolute;top:3641px;width:34px;height:34px;border-radius:50%}
</style>
</head>
<body>

<header class="site-header">
  <nav class="main-nav"><span>Home</span><span>About Us</span><span>Treatments</span><span>Post-Surgery Treatment</span><span>Contact</span></nav>
  <div class="phone-box">(555) 214-3870</div>
</header>
<div class="brand-tab"><span class="dot"></span><span class="name">Glow 742</span></div>

<section>
  <div class="fill hero-photo" role="img" aria-label="Woman with towel on her head, eyes closed, hands framing her face, green bamboo leaves behind"></div>
  <svg class="abs hero-wave" viewBox="0 0 1200 160" preserveAspectRatio="none">
    <path d="M0 20 C220 130 420 150 600 90 C780 30 960 10 1200 60 L1200 160 L0 160Z" fill="var(--brown)"/>
    <path d="M0 40 C230 170 430 150 610 110 C790 60 980 50 1200 80 L1200 160 L0 160Z" fill="var(--cream)"/>
  </svg>
  <div class="abs welcome-box">
    <h1 class="script">Welcome to Glow 742 Skin Lounge<br>and Post Liposuction Care</h1>
    <div class="btn" style="left:167px;top:126px;width:154px;height:50px">Get Started</div>
  </div>
</section>

<section>
  <h2 class="abs section-title script about-title">About <span>Us</span></h2>
  <div class="abs body-copy about-copy">
    <p>You deserve more, whether it’s a suite of services that treats every bodily need, a top-notch professional staff or a relaxing venue to enjoy them in. This is where We shine. Here, you can take your pick of from a variety of beauty-boosting services.</p>
    <p>We use Peruvian natural products. For instance, the Skin Care Body Wraps, which are tailored to relax the body, detoxify, exfoliate &amp; hydrate the skin, all while helping you to lose inches.</p>
  </div>
  <div class="btn" style="left:112px;top:1148px;width:145px;height:51px">Learn More</div>
  <div class="abs about-frame"></div>
  <div class="abs about-photo"><div role="img" aria-label="Spa reception wall with painted lounge sign, sliding dark glass door and potted plants"></div></div>
</section>

<section>
  <div class="abs treat-band"></div>
  <h2 class="abs treat-title script">Our Treatments</h2>
  <div class="round-arrow" style="left:1011px;top:1366px"><svg width="12" height="12" viewBox="0 0 12 12"><path d="M8 1 3 6l5 5" fill="none" stroke="#333" stroke-width="1.8"/></svg></div>
  <div class="round-arrow" style="left:1053px;top:1366px"><svg width="12" height="12" viewBox="0 0 12 12"><path d="M4 1l5 5-5 5" fill="none" stroke="#333" stroke-width="1.8"/></svg></div>

  <div class="treat-card" style="left:112px;background:linear-gradient(160deg,#5a4a40 0%,#cfc8c0 40%,#f1efed 70%,#bdb6ae 100%)" role="img" aria-label="Therapist performing microdermabrasion on a client in a treatment room">
    <div class="label">Diamond<br>Microdermoabrasion</div>
  </div>
  <div class="treat-card featured" style="left:444px">
    <svg class="treat-icon" width="60" height="64" viewBox="0 0 60 64" fill="none" stroke="#fff" stroke-width="2">
      <rect x="6" y="4" width="14" height="20" rx="3" transform="rotate(-40 13 14)"/>
      <path d="M18 22l12 14"/>
      <circle cx="33" cy="40" r="6"/>
      <path d="M44 36c4 6 2 14-4 18M50 34c5 9 2 20-8 25"/>
    </svg>
    <h3>Ultrasound Cavitation</h3>
    <p>Body sculpting treatment with no anesthesia, no scars, no discomfort, no down-time and presents a risk-free alternative to liposuction.</p>
    <a>LEARN MORE</a>
  </div>
  <div class="treat-card" style="left:775px;background:linear-gradient(150deg,#a8d24a 0%,#cfe58e 40%,#e8d9b8 65%,#7fb63a 100%)" role="img" aria-label="Woman with flowers in her hair holding a white lily against a green background">
    <div class="label">Glow 742 Facials</div>
  </div>
</section>

<section>
  <div class="abs post-frame"></div>
  <div class="abs post-photo"><div role="img" aria-label="Hands massaging a client's abdomen during post-surgery treatment"></div></div>
  <h2 class="abs section-title script post-title">Post-Surgery <span>Treatment</span></h2>
  <p class="abs body-copy post-copy">The post-surgery treatment is a combination of techniques that speed up the patient’s healing process after surgery. Its main objective is to eliminate the surgery’s inflammation and correct the skin irregularities produced by Fibrosis. Fibrosis is an effect suffered by most patients after surgery. If the patient notices hardening of the skin tissues, lumps or deformations in the area that was subjected to surgery</p>
  <div class="btn" style="left:672px;top:2180px;width:145px;height:49px">Learn More</div>
</section>

<section>
  <div class="abs ba-band"></div>
  <h2 class="abs ba-title script">Before &amp; After</h2>
  <svg class="abs" style="left:84px;top:2610px" width="20" height="28" viewBox="0 0 20 28"><path d="M15 2 4 14l11 12" fill="none" stroke="#fff" stroke-width="3"/></svg>
  <svg class="abs" style="left:1096px;top:2610px" width="20" height="28" viewBox="0 0 20 28"><path d="M5 2l11 12L5 26" fill="none" stroke="#fff" stroke-width="3"/></svg>
  <div class="ba-card" style="left:163px"><div class="shot" role="img" aria-label="Client portrait before treatment"></div><div class="cap">BEFORE</div></div>
  <div class="ba-card" style="left:609px"><div class="shot" role="img" aria-label="Client portrait after treatment"></div><div class="cap">AFTER</div></div>
</section>

<section>
  <h2 class="abs news-title script">Subscribe <span>Our Newsletter</span></h2>
  <p class="abs news-sub">Get 10% off your first treatment when you subscribe!</p>
  <div class="abs news-form"><div class="field">Email Address</div><div class="submit">Subscribe</div></div>
</section>

<footer>
  <svg class="abs footer-wave" viewBox="0 0 1200 514" preserveAspectRatio="none">
    <path d="M0 40 C160 150 330 170 520 110 C720 40 900 -10 1200 50 L1200 514 L0 514Z" fill="var(--brown)"/>
    <path d="M0 60 C170 180 350 190 540 130 C740 70 930 40 1200 90 L1200 514 L0 514Z" fill="var(--ink)"/>
  </svg>
  <nav class="abs footer-nav"><span>Home</span><span>About Us</span><span>Treatments</span><span>Post-Surgery Treatment</span><span>Contact</span></nav>
  <div class="footer-rule" style="left:112px;top:3439px;width:385px"></div>
  <div class="footer-rule" style="left:703px;top:3439px;width:385px"></div>
  <div class="abs footer-brand"><span class="dot"></span><span class="name">Glow 742</span></div>
  <div class="footer-divider" style="left:436px"></div>
  <div class="footer-divider" style="left:762px"></div>
  <div class="footer-col" style="left:112px">
    <svg width="16" height="22" viewBox="0 0 16 22"><path d="M8 0a8 8 0 0 0-8 8c0 6 8 14 8 14s8-8 8-14a8 8 0 0 0-8-8zm0 11a3 3 0 1 1 0-6 3 3 0 0 1 0 6z" fill="var(--brown)"/></svg>
    18 Alder Court Fairview<br>CT 06100
  </div>
  <div class="footer-col" style="left:437px">
    <svg width="26" height="20" viewBox="0 0 26 20"><rect width="26" height="20" rx="2" fill="var(--brown)"/><path d="M1 2l12 9 12-9" fill="none" stroke="var(--ink)" stroke-width="2"/></svg>
    glow742spa@mailbox.com
  </div>
  <div class="footer-col" style="left:763px">
    <svg width="22" height="22" viewBox="0 0 22 22"><path d="M4 1l4 1 1 5-3 2a13 13 0 0 0 7 7l2-3 5 1 1 4c0 2-2 3-4 3C9 21 1 13 1 5c0-2 1-4 3-4z" fill="var(--brown)"/></svg>
    (555) 214-3870 or<br>(555) 214-3921
  </div>
  <div class="footer-rule" style="left:112px;top:3628px;width:976px"></div>
  <p class="abs copyright">© 2021 Glow 742. All Rights Reserved &nbsp; | &nbsp; Privacy Policy</p>
  <div class="social" style="left:1011px;background:var(--brown)" aria-label="Social profile"></div>
  <div class="social" style="left:1053px;background:var(--white)" aria-label="Social profile"></div>
</footer>

</body>
</html>
```